Beneath the Quiet Orchards

Beneath the Quiet Orchards ", Author: Colette Bramard Size: 16 x 24 cm The publisher" Editions Varonne "should be placed on the bottom, with Gill without light Font The books is the portraits of women who had a lover younger or much younger than them

Target Market(s)

General Public

Colors

Designer to choose colors to be used in the design.

Requirements
Must have
• The 11 portraits

```html
<!DOCTYPE html>
<html lang="en">
<head>
<meta charset="utf-8">
<title>Beneath the Quiet Orchards — Colette Bramard</title>
<link href="https://fonts.googleapis.com/css2?family=Open+Sans:wght@300;400;600;700&display=swap" rel="stylesheet">
<style>
  :root {
    --page-bg: #dfe5e9;
    --cover-top: #5f5f5f;
    --cover-mid: #8f9092;
    --cover-bottom: #6b6b6b;
    --ink-light: #ffffff;
    --portrait-dark: #1c1c1c;
    --portrait-mid: #6e6e6e;
    --portrait-edge: #d8d8d8;
  }
  * { margin: 0; padding: 0; box-sizing: border-box; }
  html, body {
    width: 1200px; height: 1200px; overflow: hidden;
    background: var(--page-bg);
    font-family: "Open Sans", sans-serif;
  }
  .book-cover {
    position: absolute; left: 260px; top: 90px;
    width: 680px; height: 1020px;
    background: radial-gradient(ellipse 70% 55% at 50% 72%, var(--cover-mid) 0%, var(--cover-bottom) 70%),
                linear-gradient(180deg, var(--cover-top), var(--cover-bottom));
    background-blend-mode: normal;
    color: var(--ink-light);
    text-align: center;
    box-shadow: 0 6px 24px rgba(0,0,0,0.18);
  }
  .author-name {
    position: absolute; left: 0; right: 0; top: 58px;
    font-size: 46px; font-weight: 600; letter-spacing: -0.5px;
  }
  .portrait-wall { position: absolute; inset: 0; }
  .portrait {
    position: absolute;
    background: radial-gradient(ellipse at 50% 40%, var(--portrait-mid), var(--portrait-dark) 80%);
    border: 2px solid var(--portrait-edge);
    box-shadow: 0 2px 6px rgba(0,0,0,0.35);
  }
  .title-lead {
    position: absolute; left: 0; right: 0; top: 662px;
    font-size: 39px; font-weight: 300;
  }
  .title-main {
    position: absolute; left: 0; right: 0; top: 718px;
    font-size: 62px; font-weight: 700; line-height: 76px; letter-spacing: -0.5px;
  }
  .publisher {
    position: absolute; left: 0; right: 0; top: 928px;
    font-size: 30px; font-weight: 300;
  }
</style>
</head>
<body>
  <main class="book-cover">
    <div class="author-name">Colette Bramard</div>

    <div class="portrait-wall">
      <div class="portrait" role="img" aria-label="Black and white portrait of a woman" style="left:203px;top:200px;width:91px;height:95px"></div>
      <div class="portrait" role="img" aria-label="Black and white portrait of a smiling woman" style="left:305px;top:158px;width:191px;height:137px"></div>
      <div class="portrait" role="img" aria-label="Black and white portrait of an older woman in glasses" style="left:515px;top:227px;width:90px;height:133px"></div>
      <div class="portrait" role="img" aria-label="Black and white portrait of a smiling woman" style="left:73px;top:314px;width:132px;height:182px"></div>
      <div class="portrait" role="img" aria-label="Black and white portrait of a nineteenth-century woman" style="left:221px;top:314px;width:128px;height:91px"></div>
      <div class="portrait" role="img" aria-label="Black and white portrait of a young woman" style="left:368px;top:314px;width:131px;height:182px"></div>
      <div class="portrait" role="img" aria-label="Black and white portrait of a woman with curly hair" style="left:515px;top:370px;width:90px;height:124px"></div>
      <div class="portrait" role="img" aria-label="Black and white portrait of an older woman" style="left:221px;top:422px;width:128px;height:180px"></div>
      <div class="portrait" role="img" aria-label="Black and white portrait of a woman" style="left:100px;top:510px;width:107px;height:92px"></div>
      <div class="portrait" role="img" aria-label="Black and white portrait of a woman" style="left:367px;top:510px;width:91px;height:92px"></div>
      <div class="portrait" role="img" aria-label="Black and white portrait of a smiling woman" style="left:469px;top:510px;width:88px;height:92px"></div>
    </div>

    <h1>
      <span class="title-lead">Beneath the</span>
      <span class="title-main">Quiet<br>Orchards</span>
    </h1>

    <div class="publisher">Editions Varonne</div>
  </main>
</body>
</html>
```